Electronic Time-sheet for phones

I need a time-sheet that can be accessed on the phone, be completed, then have the ability to electronically sign. The time sheet needs to be used two fold for supervision to verify hours and quantities and also for the client to be able to electronically sign. The time-sheet should be daily or weekly if we can get the data to fit. We are trying to streamline field supervisors having to log on to a computer to access a server just to do time-sheets. We need it to be user friendly. We need to have two places to have electronic signatures. One for supervisor or authorized representative and the other for the client to sign.

Target Market(s)

Industrial clients

Industry/Entity Type

Oil And Gas

Requirements
Must have
• hours, quantities, project name, location, signature line etc
Nice to have
• n/a
Should not have
• n/a

```html
<!DOCTYPE html>
<html lang="en">
<head>
<meta charset="utf-8">
<title>Supervisor: Adding/Editing an Employee's Time Sheet</title>
<link rel="stylesheet" href="https://fonts.googleapis.com/css2?family=Mulish:wght@300;400&family=Roboto:wght@400;500;700&display=swap">
<style>
  :root {
    --page-bg: #ffffff;
    --navy: #14305e;
    --ink: #111111;
    --text-grey: #555555;
    --label-grey: #5a5a5a;
    --placeholder: #6e6e6e;
    --field-border: #c9c9c9;
    --card-border: #d4d4d4;
    --divider: #bdbdbd;
    --ios-blue: #1a7cf0;
    --icon-grey: #9a9a9a;
    --scroll-track: #b9b9b9;
    --scroll-thumb: #6a6a6a;
    --tab-bg: #fafafa;
  }
  * { box-sizing: border-box; margin: 0; padding: 0; }
  html, body { width: 1200px; height: 1000px; overflow: hidden; background: var(--page-bg); }
  body { position: relative; font-family: "Roboto", Arial, sans-serif; }

  /* Annotation */
  .step-badge {
    position: absolute; left: 291px; top: 266px; width: 46px; height: 46px;
    border-radius: 50%; background: var(--navy); color: #fff;
    font: 400 14px/46px "Mulish", sans-serif; text-align: center;
  }
  .note { position: absolute; left: 199px; top: 336px; width: 330px; color: var(--ink); font-family: "Mulish", sans-serif; }
  .note-title { font-weight: 300; font-size: 30px; line-height: 37.5px; }
  .note-body { font-weight: 400; font-size: 16.5px; line-height: 18.8px; margin-top: -6px; }

  /* App screen */
  .screen {
    position: absolute; left: 569px; top: 142px; width: 410px; height: 693px;
    background: #fff; border: 1px solid #dcdcdc; overflow: hidden;
  }
  .status-bar {
    position: absolute; left: 0; top: 0; width: 100%; height: 20px;
    font-size: 12px; color: #000; display: flex; align-items: center;
  }
  .status-left { position: absolute; left: 6px; display: flex; align-items: center; gap: 4px; }
  .status-time { position: absolute; left: 0; right: 0; text-align: center; font-weight: 500; }
  .status-right { position: absolute; right: 4px; display: flex; align-items: center; gap: 4px; }

  .nav-back {
    position: absolute; left: 16px; top: 43px; color: var(--ios-blue);
    font-size: 18px; display: flex; align-items: center; gap: 5px;
  }
  .brand-name {
    position: absolute; right: 16px; top: 42px; color: var(--navy);
    font: 700 30px/1 "Roboto", sans-serif; letter-spacing: 0.5px;
  }

  .card {
    position: absolute; left: 17px; top: 99px; width: 376px; height: 526px;
    border: 1px solid var(--card-border); border-radius: 6px;
  }
  .card-header {
    position: absolute; left: 13px; right: 13px; top: 0; height: 60px;
    border-bottom: 1px solid var(--divider); font-size: 14.5px; color: var(--text-grey);
  }
  .header-employee { position: absolute; left: 0; top: 18px; display: flex; align-items: center; gap: 9px; }
  .header-date { position: absolute; right: 2px; top: 20px; display: flex; align-items: center; gap: 9px; }

  .section-label {
    position: absolute; left: 13px; font-weight: 700; font-size: 14.5px; color: var(--label-grey);
  }
  .field {
    position: absolute; left: 13px; width: 324px; height: 41px;
    border: 1px solid var(--field-border); border-radius: 4px;
    padding-left: 11px; font-size: 14.5px; line-height: 39px; color: var(--placeholder);
  }

  .scroll-track { position: absolute; left: 363px; top: 70px; width: 5px; height: 450px; border-radius: 3px; background: var(--scroll-track); }
  .scroll-thumb { position: absolute; left: 0; top: 0; width: 5px; height: 165px; border-radius: 3px; background: var(--scroll-thumb); }

  .tab-bar {
    position: absolute; left: 0; bottom: 0; width: 100%; height: 54px;
    background: var(--tab-bg); border-top: 1px solid #ececec;
  }
  .tab { position: absolute; top: 6px; width: 100px; text-align: center; font-size: 8.5px; color: #444; }
  .tab svg { display: block; margin: 0 auto 3px; }
  .tab.is-active { color: var(--ios-blue); }
</style>
</head>
<body>

  <div class="step-badge">5</div>
  <div class="note">
    <h1 class="note-title">Supervisor:<br>Adding/Editing<br>an Employee's<br>Time Sheet</h1>
    <p class="note-body">All the required parameters<br>required against an employee<br>can be displayed as follows.<br>A scroll bar will be required<br>to view more fields.<br>At the bottom of this page,<br>two buttons can be provided.<br>"Save" and "Sign". Save will just<br>store the entered information.<br>Signing it will store as well as<br>approve this employee's time sheet.<br>Once all employees in a time<br>sheet have been signed, a<br>green tick symbol next to the<br>supervisor icon will display<br>against this time sheet (show in<br>screen 3)</p>
  </div>

  <main class="screen">
    <div class="status-bar">
      <div class="status-left">
        <svg width="34" height="6" viewBox="0 0 34 6" aria-hidden="true">
          <circle cx="3" cy="3" r="2.6" fill="#000"/><circle cx="9.5" cy="3" r="2.6" fill="#000"/><circle cx="16" cy="3" r="2.6" fill="#000"/>
          <circle cx="22.5" cy="3" r="2.3" fill="none" stroke="#000" stroke-width="0.7"/><circle cx="29" cy="3" r="2.3" fill="none" stroke="#000" stroke-width="0.7"/>
        </svg>
        <span>GS</span>
        <svg width="12" height="9" viewBox="0 0 12 9" aria-hidden="true">
          <path d="M1 3.2a7 7 0 0 1 10 0M2.8 5a4.4 4.4 0 0 1 6.4 0" fill="none" stroke="#000" stroke-width="1.3"/><circle cx="6" cy="7.4" r="1.2" fill="#000"/>
        </svg>
      </div>
      <div class="status-time">9:41 AM</div>
      <div class="status-right">
        <svg width="7" height="11" viewBox="0 0 7 11" aria-hidden="true"><path d="M1 3l5 5-2.5 2V1L6 3 1 8" fill="none" stroke="#444" stroke-width="0.9"/></svg>
        <span>58 %</span>
        <svg width="25" height="11" viewBox="0 0 25 11" aria-hidden="true"><rect x="0.5" y="0.5" width="21" height="10" rx="2" fill="none" stroke="#000"/><rect x="2" y="2" width="11" height="7" fill="#000"/><rect x="22.5" y="3.5" width="2" height="4" fill="#000"/></svg>
      </div>
    </div>

    <div class="nav-back">
      <svg width="9" height="15" viewBox="0 0 9 15" aria-hidden="true"><path d="M7.5 1.5 2 7.5l5.5 6" fill="none" stroke="currentColor" stroke-width="2"/></svg>
      <span>Go Back</span>
    </div>
    <div class="brand-name">KESTREL</div>

    <section class="card">
      <div class="card-header">
        <div class="header-employee">
          <svg width="32" height="32" viewBox="0 0 32 32" aria-hidden="true">
            <circle cx="16" cy="16" r="15" fill="none" stroke="#666" stroke-width="1.5"/>
            <circle cx="16" cy="12" r="5.5" fill="#666"/>
            <path d="M6.5 27c1.5-6 5-8 9.5-8s8 2 9.5 8a14 14 0 0 1-19 0z" fill="#666"/>
          </svg>
          <span>New Employee</span>
        </div>
        <div class="header-date">
          <svg width="18" height="26" viewBox="0 0 18 26" aria-hidden="true"><path d="M6 1h11v24H1V6z" fill="none" stroke="#999" stroke-width="1.6"/><path d="M6 1v5H1" fill="none" stroke="#999" stroke-width="1.6"/></svg>
          <span>5 November, 2018</span>
        </div>
      </div>

      <h2 class="section-label" style="top:82px">Employee Details</h2>
      <div class="field" style="top:121px">Enter Employee Name</div>
      <div class="field" style="top:184px">Enter Employee No.</div>

      <h2 class="section-label" style="top:238px">Project Details</h2>
      <div class="field" style="top:270px">Enter Project Name</div>
      <div class="field" style="top:333px">Enter Project No.</div>
      <div class="field" style="top:396px">Enter Client Name</div>
      <div class="field" style="top:458px">Enter Client Location</div>

      <div class="scroll-track"><div class="scroll-thumb"></div></div>
    </section>

    <nav class="tab-bar">
      <div class="tab is-active" style="left:20px">
        <svg width="20" height="27" viewBox="0 0 20 27" aria-hidden="true"><path d="M7 1.5h11v24H2V7z" fill="none" stroke="currentColor" stroke-width="2.2"/><path d="M7 1.5V7H2" fill="none" stroke="currentColor" stroke-width="2"/></svg>
        Current Week
      </div>
      <div class="tab" style="left:148px">
        <svg width="32" height="27" viewBox="0 0 32 27" aria-hidden="true"><path d="M8 13.5a10.5 10.5 0 1 1 3 7.3" fill="none" stroke="var(--icon-grey)" stroke-width="2"/><path d="M4 11l4 4 4-4" fill="none" stroke="var(--icon-grey)" stroke-width="2"/><rect x="14" y="9" width="8" height="10" fill="none" stroke="var(--icon-grey)" stroke-width="1.6"/></svg>
        History
      </div>
      <div class="tab" style="left:280px">
        <svg width="32" height="27" viewBox="0 0 32 27" aria-hidden="true"><path d="M10 5.5a11 11 0 1 0 12 0" fill="none" stroke="var(--icon-grey)" stroke-width="2.4"/><path d="M16 1.5v11" stroke="var(--icon-grey)" stroke-width="2.6"/></svg>
        Logout
      </div>
    </nav>
  </main>

</body>
</html>
```